Salve Label

2.25 inch round label.

We are looking for a simple label, muted natural colors, sophisticated, elegant, calming.

Name of Product: Herbal Beeswax Salve
This scent is lavender - but there will be others scents
Want this label to be adaptable to other scents with simple color and word changes.

Other things to express on the label - all natural, calming, relaxing

Name of the Company: Copper Hollow Farm
2 oz.

```html
<!DOCTYPE html>
<html lang="en">
<head>
<meta charset="utf-8">
<title>Lavender Herbal Beeswax Salve Label</title>
<link href="https://fonts.googleapis.com/css2?family=Merriweather:wght@900&family=Montserrat:wght@400;500&display=swap" rel="stylesheet">
<style>
  :root {
    --paper: #ffffff;
    --label-white: #f6f6f6;
    --ink: #1c1c1c;
    --lavender: #8436dc;
    --lavender-soft: #e6d9f2;
    --silver-light: #f2f2f2;
    --silver-mid: #c4c6c8;
    --silver-dark: #8d9093;
    --backdrop: #f2dce8;
  }
  html, body {
    margin: 0;
    padding: 0;
    width: 1200px;
    height: 2403px;
    overflow: hidden;
    background: var(--paper);
  }
  .canvas {
    position: relative;
    width: 1200px;
    height: 2403px;
  }
  .label-sheet {
    position: absolute;
    left: 0;
    top: 0;
    width: 1200px;
    height: 1200px;
    background: var(--paper);
  }
  .label {
    display: block;
    width: 1200px;
    height: 1200px;
  }
  .backdrop {
    position: absolute;
    left: 0;
    top: 1280px;
    width: 1200px;
    height: 1123px;
    background: var(--backdrop);
  }
  .farm-name {
    font-family: "Montserrat", sans-serif;
    font-weight: 500;
    font-size: 50px;
    fill: var(--ink);
  }
  .scent-name {
    font-family: "Merriweather", serif;
    font-weight: 900;
    font-size: 138px;
    fill: var(--lavender);
  }
  .product-line {
    font-family: "Montserrat", sans-serif;
    font-weight: 400;
    font-size: 58px;
    letter-spacing: 8px;
    fill: var(--ink);
  }
  .product-name {
    font-family: "Merriweather", serif;
    font-weight: 900;
    font-size: 68px;
    letter-spacing: 1px;
    fill: var(--ink);
  }
  .net-weight-label {
    font-family: "Montserrat", sans-serif;
    font-weight: 400;
    font-size: 28px;
    fill: var(--paper);
  }
  .net-weight-value {
    font-family: "Montserrat", sans-serif;
    font-weight: 400;
    font-size: 54px;
    fill: var(--paper);
  }
</style>
</head>
<body>
<main class="canvas">
  <section class="label-sheet">
    <svg class="label" viewBox="0 0 1200 1200" xmlns="http://www.w3.org/2000/svg">
      <defs>
        <linearGradient id="silver-rim" x1="0" y1="0" x2="1" y2="1">
          <stop offset="0" stop-color="var(--silver-light)"/>
          <stop offset="0.3" stop-color="var(--silver-dark)"/>
          <stop offset="0.55" stop-color="var(--silver-light)"/>
          <stop offset="0.8" stop-color="var(--silver-mid)"/>
          <stop offset="1" stop-color="var(--silver-dark)"/>
        </linearGradient>
        <clipPath id="label-face">
          <circle cx="600" cy="592" r="510"/>
        </clipPath>
        <path id="farm-arc" d="M 200 640 A 400 400 0 0 1 1000 640"/>
      </defs>

      <circle class="rim" cx="600" cy="592" r="572" fill="url(#silver-rim)"/>
      <circle class="face" cx="600" cy="592" r="510" fill="var(--label-white)"/>

      <path class="arc-band" d="M 215 520 A 412 412 0 0 1 318 340" fill="none" stroke="var(--ink)" stroke-width="14"/>
      <path class="arc-band" d="M 882 340 A 412 412 0 0 1 985 520" fill="none" stroke="var(--ink)" stroke-width="14"/>
      <text class="farm-name"><textPath href="#farm-arc" startOffset="50%" text-anchor="middle" textLength="540" lengthAdjust="spacing">Copper Hollow Farm</textPath></text>

      <path class="sprig-illustration" role="img" aria-label="Faint lavender sprig illustration" d="M 800 560 C 860 430 960 440 950 560 C 940 700 880 840 790 960 C 770 820 760 680 800 560 Z" fill="var(--lavender-soft)" opacity="0.7"/>

      <ellipse class="bee-illustration" role="img" aria-label="Black line illustration of a honeybee with spread wings" cx="600" cy="410" rx="230" ry="115" fill="#d9d9d9"/>

      <text class="scent-name" x="600" y="640" text-anchor="middle">lavender</text>
      <line x1="342" y1="745" x2="448" y2="745" stroke="var(--ink)" stroke-width="5"/>
      <text class="product-line" x="604" y="766" text-anchor="middle">HERBAL</text>
      <line x1="758" y1="745" x2="864" y2="745" stroke="var(--ink)" stroke-width="5"/>
      <text class="product-name" x="600" y="856" text-anchor="middle">BEESWAX SALVE</text>

      <rect class="weight-band" x="0" y="906" width="1200" height="300" fill="var(--lavender)" clip-path="url(#label-face)"/>
      <text class="net-weight-label" x="600" y="962" text-anchor="middle">NET WEIGHT</text>
      <text class="net-weight-value" x="600" y="1020" text-anchor="middle">2oz / 56.7g</text>
    </svg>
  </section>
  <div class="backdrop"></div>
</main>
</body>
</html>
```